Social Media Graphics - ALL TEXT RK

We are looking for a series of social media graphics for Instagram (standard size 1:1 (1080x1080px) that are ALL TEXT. We want the following quotes below on each graphic; one quote per graphic. AND, In very small letters at the bottom of each graphic, add @RKMarlowLive

The look and feel of these graphics should be complimentary to the color palette attached below; but keep them simple. But the design is up to you; at the end of this document, I provided various samples of all text graphics that I like as examples.

Target Market(s)

women looking to lose weight

Industry/Entity Type

health and wellness

Colors
E54698
E96AAD
F1A4CE
F9D9EA
FCEFF6

Requirements
Must have
• the quotes in the document
Should not have
• no stock photography

```html
<!DOCTYPE html>
<html lang="en">
<head>
<meta charset="utf-8">
<title>RK Social Graphics – All Text Series</title>
<link href="https://fonts.googleapis.com/css2?family=Arimo:ital,wght@0,400;0,700;1,700&family=Anton&family=Montserrat:wght@800&family=Roboto+Condensed:ital,wght@0,400;0,700;0,900;1,700;1,900&family=Permanent+Marker&display=swap" rel="stylesheet">
<style>
  :root{
    --magenta-deep:#cc0066;
    --magenta:#e6007e;
    --hot-pink:#ff3d9f;
    --pink-mid:#f99bd3;
    --pink-soft:#fcd0e6;
    --blush:#ffd6ea;
    --white:#ffffff;
    --paper:#f1f1f1;
  }
  *{margin:0;padding:0;box-sizing:border-box}
  html,body{width:923px;height:1200px;overflow:hidden;background:var(--white)}
  .sheet{position:relative;width:923px;height:1200px}
  .post{position:absolute;width:271px;height:271px;overflow:hidden}
  .handle{position:absolute;left:0;right:0;top:293px;bottom:0;}
  .post .handle{top:auto;bottom:7px;text-align:center;font:700 7.2px/1 "Arimo",sans-serif;color:var(--white)}
  .handle--dark{color:var(--magenta)!important}

  /* positions */
  .c1{left:37px}.c2{left:326px}.c3{left:614px}
  .r1{top:39px}.r2{top:323px}.r3{top:607px}.r4{top:891px}

  /* 1 */
  .overnight{background:radial-gradient(circle at 82% 40%,#ffe0f0 0,#ff7ab8 22%,#ff0a85 48%,#d20068 80%)}
  .overnight p{position:absolute;left:18px;top:72px;width:180px;font:700 16.6px/1.32 "Arimo",sans-serif;color:var(--white)}

  /* 2 */
  .struggling{background:linear-gradient(180deg,#ff4ca6 0%,#ff1b8f 60%,#ff0a85 100%);text-align:center;color:var(--white)}
  .struggling h2{position:absolute;left:10px;right:10px;top:52px;font:400 25px/0.93 "Anton",sans-serif;letter-spacing:.2px}
  .struggling p{position:absolute;left:8px;right:8px;top:148px;font:400 18px/1.28 "Anton",sans-serif;letter-spacing:.2px}

  /* 3 */
  .one-night{background:var(--pink-soft);color:var(--magenta-deep)}
  .one-night h2{position:absolute;left:25px;top:55px;font:700 25px/.88 "Arimo",sans-serif;letter-spacing:-1.3px;transform:scaleX(.93);transform-origin:left}
  .one-night p{position:absolute;left:0;right:0;top:130px;text-align:center;font:700 15.5px/1.3 "Arimo",sans-serif}
  .one-night .arrow{position:absolute;left:30px;top:170px}
  .one-night .cta{position:absolute;left:65px;top:188px;font:700 14.5px/1 "Arimo",sans-serif}
  .one-night .underline{position:absolute;left:63px;top:207px}

  /* 4 */
  .flattens{background:var(--hot-pink)}
  .flattens .tag{position:absolute;left:14px;top:77px;width:242px;height:124px;background:var(--magenta-deep);transform:rotate(-2deg);box-shadow:-3px 3px 0 #8c0046;display:flex;align-items:center;justify-content:center;text-align:center}
  .flattens .tag p{font:800 16.4px/1.33 "Montserrat",sans-serif;color:var(--white);padding:0 10px}

  /* 5 */
  .hormones{background:var(--magenta-deep);text-align:center}
  .hormones h2{position:absolute;left:8px;right:8px;top:54px;font:900 italic 26.5px/1.02 "Roboto Condensed",sans-serif;color:var(--blush);letter-spacing:-.4px;text-transform:uppercase}

  /* 6 */
  .frustrated{background:radial-gradient(circle at 30% 30%,#fbfbfb 0,#ececec 60%,#e2e2e2 100%);color:var(--magenta-deep);text-align:center}
  .frustrated .note{position:absolute;left:12px;right:6px;top:30px;transform:rotate(-7deg);font:400 19px/1.2 "Permanent Marker",cursive}
  .frustrated .note span{display:block;margin-top:14px}

  /* 7 */
  .not-your-fault{background:var(--pink-mid);text-align:center}
  .not-your-fault h2{position:absolute;left:4px;right:4px;top:52px;font:700 33px/0.99 "Roboto Condensed",sans-serif;color:var(--magenta-deep);text-shadow:1.5px 1.5px 0 var(--white)}

  /* 8 */
  .lied-to{background:radial-gradient(ellipse 90% 45% at 50% 0%,#ff6fb5 0,#fcbedc 55%,var(--pink-soft) 80%);text-align:center}
  .lied-to h2{position:absolute;left:0;right:0;top:56px;font:700 25.5px/1 "Roboto Condensed",sans-serif;color:var(--magenta)}
  .lied-to p{position:absolute;left:0;right:0;top:118px;font:700 24.5px/1.27 "Roboto Condensed",sans-serif;color:var(--magenta)}
  .lied-to em{color:#f77cb9;font-style:italic}

  /* 9 */
  .glp-natural{background:radial-gradient(circle at 50% 40%,#f9a6d8 0,var(--pink-mid) 70%,#f58ccb 100%);color:var(--white)}
  .glp-natural h2{position:absolute;left:0;right:0;top:34px;text-align:center;font:700 25px/.9 "Roboto Condensed",sans-serif}
  .glp-natural h2 b{color:var(--magenta-deep)}
  .glp-natural ul{position:absolute;left:23px;top:108px;list-style:none;font:400 19px/1.38 "Roboto Condensed",sans-serif}
  .glp-natural li.strong{font-weight:700;color:var(--magenta-deep)}
  .glp-natural .cta{position:absolute;left:0;right:0;top:212px;text-align:center;font:700 italic 19px/1 "Roboto Condensed",sans-serif;color:var(--magenta-deep)}

  /* 10 */
  .glp-secret{background:radial-gradient(ellipse at 50% 50%,#e60f7a 0,#f23b96 55%,#f76ab0 100%);color:var(--white);text-align:center}
  .glp-secret h2{position:absolute;left:0;right:0;top:45px;font:900 italic 22px/1 "Roboto Condensed",sans-serif;letter-spacing:1px}
  .glp-secret .lede{position:absolute;left:0;right:0;top:99px;font:700 17.5px/1.25 "Arimo",sans-serif}
  .glp-secret .label{position:absolute;left:19px;width:233px;top:153px;height:23px;background:var(--white);color:var(--magenta-deep);font:700 15.5px/23px "Arimo",sans-serif;letter-spacing:.8px}
  .glp-secret .reveal{position:absolute;left:0;right:0;top:178px;font:700 17.3px/1.25 "Arimo",sans-serif}
</style>
</head>
<body>
<main class="sheet">

  <section class="post overnight c1 r1">
    <p>Wake up tomorrow with a flatter belly- Yes, this overnight remedy works like magic!</p>
    <span class="handle">@RKMarlowLive</span>
  </section>

  <section class="post struggling c2 r1">
    <h2>STRUGGLING WITH<br>BLOATING AND BELLY<br>FAT?</h2>
    <p>TRY THIS NATURAL<br>SOLUTION TONIGHT, AND<br>WAKE UP FEELING LIGHTER!</p>
    <span class="handle">@RKMarlowLive</span>
  </section>

  <section class="post one-night c3 r1">
    <h2>ONE SUPPLEMENT,<br>ONE NIGHT;</h2>
    <p>Your belly bloat could be<br>gone by morning.</p>
    <svg class="arrow" width="30" height="42" viewBox="0 0 30 42" aria-hidden="true">
      <path d="M8 2 C0 14 2 30 22 34" fill="none" stroke="#cc0066" stroke-width="2" stroke-linecap="round"/>
      <path d="M16 27 L23 34 L16 40" fill="none" stroke="#cc0066" stroke-width="2" stroke-linecap="round" stroke-linejoin="round"/>
    </svg>
    <span class="cta">Here's how it works!</span>
    <svg class="underline" width="140" height="6" viewBox="0 0 140 6" aria-hidden="true">
      <path d="M2 4 C40 2 100 1 138 3" fill="none" stroke="#cc0066" stroke-width="2" stroke-linecap="round"/>
    </svg>
    <span class="handle handle--dark">@RKMarlowLive</span>
  </section>

  <section class="post flattens c1 r2">
    <div class="tag"><p>Finally-a natural solution that flattens your belly AND eases stomach bloat</p></div>
    <span class="handle">@RKMarlowLive</span>
  </section>

  <section class="post hormones c2 r2">
    <h2>Sis, your<br>hormones are<br>out of whack -<br>that's why the<br>weight won't<br>budge!</h2>
    <span class="handle">@RKMarlowLive</span>
  </section>

  <section class="post frustrated c3 r2">
    <div class="note">FRUSTRATED WITH BELLY FAT THAT WON'T BUDGE?<span>I'VE GOT THE SOLUTION THAT FINALLY WORKED FOR ME-NO CRAZY DIETS REQUIRED.</span></div>
    <span class="handle handle--dark">@RKMarlowLive</span>
  </section>

  <section class="post not-your-fault c1 r3">
    <h2>THAT STUBBORN<br>BELLY FAT ISN'T<br>YOUR FAULT -<br>HERE'S WHAT NO<br>ONE TELLS YOU.</h2>
    <span class="handle handle--dark">@RKMarlowLive</span>
  </section>

  <section class="post lied-to c2 r3">
    <h2>YOU'VE BEEN LIED TO</h2>
    <p><em>'just eat less and<br>exercise more'</em> doesn't<br>work in menopause</p>
    <span class="handle handle--dark">@RKMarlowLive</span>
  </section>

  <section class="post glp-natural c3 r3">
    <h2>A NATURAL WAY TO<br>BOOST <b>GLP-1</b></h2>
    <ul>
      <li>No injections.</li>
      <li>No side effects.</li>
      <li class="strong">JUST REAL RESULTS.</li>
    </ul>
    <span class="cta">Here's how it works</span>
    <span class="handle">@RKMarlowLive</span>
  </section>

  <section class="post glp-secret c2 r4">
    <h2>GLP-1</h2>
    <p class="lede">The magic behind the<br>weight loss drugs.</p>
    <div class="label">BUT HERE'S THE SECRET</div>
    <p class="reveal">You can boost it naturally<br>without a prescription!</p>
    <span class="handle">@RKMarlowLive</span>
  </section>

</main>
</body>
</html>
```